Business Card Design

Art work over image with business name and phone number. We do automotive wire repair. Some sort of auto theme. Thanks!
Updates

I would like to see the images I uploaded in the card.  Thanks!

Target Market(s)

Auto body repair shops

Industry/Entity Type

Automotive

Contact Information for Business Card

CIRCUIT BARON

480-395-2146

Requirements
Nice to have
• Raised lettering?

```html
<!DOCTYPE html>
<html lang="en">
<head>
<meta charset="utf-8">
<title>Circuit Baron Business Card</title>
<link href="https://fonts.googleapis.com/css2?family=Orbitron:wght@700&display=swap" rel="stylesheet">
<style>
  :root {
    --backdrop: #2b2b2e;
    --card-black: #050507;
    --navy-deep: #25264f;
    --navy-light: #45468a;
    --teal: #3f6671;
    --teal-light: #5a828c;
    --silver: #d9dde3;
    --text-white: #f4f5f8;
    --accent-blue: #3aa6e8;
    --xray-light: #b7bcc6;
    --xray-dark: #1a1c22;
  }
  * { margin: 0; padding: 0; box-sizing: border-box; }
  html, body { width: 1200px; height: 1000px; overflow: hidden; }
  body {
    background: var(--backdrop);
    font-family: "Orbitron", sans-serif;
    position: relative;
  }
  .card {
    position: absolute;
    top: 351px;
    width: 525px;
    height: 300px;
    border-radius: 4px;
    overflow: hidden;
    box-shadow: 0 10px 24px rgba(0,0,0,0.45);
  }
  .card-back { left: 50px; background: var(--card-black); }
  .card-front { left: 625px; background: var(--teal); }

  .car-illustration {
    position: absolute;
    left: 40px; top: 30px;
    width: 445px; height: 240px;
    border-radius: 40% 45% 40% 45%;
    background: radial-gradient(ellipse at 50% 50%, var(--xray-light) 0%, #6d727d 45%, var(--xray-dark) 80%, transparent 100%);
    opacity: 0.75;
  }
  .brand-mark {
    position: absolute;
    display: flex;
    align-items: center;
    gap: 10px;
    color: var(--text-white);
    font-weight: 700;
    letter-spacing: 2px;
    white-space: nowrap;
  }
  .brand-dot {
    width: 14px; height: 14px;
    border-radius: 50%;
    background: var(--accent-blue);
  }
  .card-back .brand-mark {
    left: 50%; top: 50%;
    transform: translate(-50%, -50%);
    font-size: 30px;
  }

  .engine-pattern {
    position: absolute;
    inset: 0;
    background: linear-gradient(135deg, var(--teal-light), var(--teal));
  }
  .front-shapes { position: absolute; inset: 0; }
  .card-front .brand-mark {
    right: 28px; top: 38px;
    font-size: 26px;
  }
  .service-line {
    position: absolute;
    left: 34px;
    color: var(--text-white);
    font-weight: 700;
    letter-spacing: 3px;
  }
  .service-line.first { top: 150px; font-size: 19px; }
  .service-line.second { top: 178px; font-size: 19px; }
  .phone-number {
    position: absolute;
    left: 34px; top: 216px;
    color: var(--text-white);
    font-size: 32px;
    font-weight: 700;
    letter-spacing: 2px;
  }
</style>
</head>
<body>
  <section class="card card-back">
    <div class="car-illustration" role="img" aria-label="X-ray style illustration of a car showing its engine and wheels"></div>
    <div class="brand-mark"><span class="brand-dot"></span>CIRCUIT BARON</div>
  </section>

  <section class="card card-front">
    <div class="engine-pattern" role="img" aria-label="Faint pattern of engine parts, pistons and brake disc in teal"></div>
    <svg class="front-shapes" width="525" height="300" viewBox="0 0 525 300">
      <defs>
        <linearGradient id="navyBand" x1="0" y1="0" x2="1" y2="1">
          <stop offset="0" stop-color="var(--navy-light)"/>
          <stop offset="1" stop-color="var(--navy-deep)"/>
        </linearGradient>
      </defs>
      <polygon points="0,0 110,0 470,300 0,300" fill="url(#navyBand)"/>
      <polygon points="110,0 132,0 492,300 470,300" fill="var(--silver)"/>
    </svg>
    <div class="brand-mark"><span class="brand-dot"></span>CIRCUIT BARON</div>
    <div class="service-line first">AUTO BODY</div>
    <div class="service-line second">REPAIR SHOP</div>
    <div class="phone-number">480-395-2146</div>
  </section>
</body>
</html>
```